Fitness Studio Grand Opening Sidewalk Poster

We need a poster designed for our new fitness studio. This will fit into an A-Frame sidewalk sign. The design should follow our color scheme of orange, grey, white.

Our logo has a gradient orange that we would like to incorporate. This is a sign that people will see as they walk by or drive by so it needs to be exciting and grab their attention in a blink of an eye.

We want this sign to drive new people to check out our business.

The logo image and text logo should be used. The "Kelta Core Fitness" text can be separated from the "sun logo symbol".

sign specs are 24x36.
I uploaded a picture of the A-Frame stand, which is orange.

The sign should read:

---start of sign text----

NOW OPEN – or – GRAND OPENING (depending on the layout)

Kelta Core Fitness (company name - in the text of the logo)

*FREE introductory class
*Personalized instruction
*Body sculpting workout
*Results training
*Fun, supportive atmosphere

1-818-555-CORE
Try A Class Today!

www.KeltaCoreFitness.example

@KeltaCoreFitness
(facebook logo, twitter logo)

----- end of sign text -----

Target Market(s)

new customers - fitness enthusiasts - woman age 30-50 - men age 40-50 -

Industry/Entity Type

Training

Font styles to use
Sans Serif

Requirements
Must have
• all the text included above - logo - work mark text
• sign should incorporate the look and feel of the logo.
• please also reference our website to get a feel of the design of the company
• www.keltacorefitness.example
Nice to have
• eye catching
• text should be easy to read while driving buy or walking
Should not have
• any other color besides the colors of the logo

```html
<!DOCTYPE html>
<html lang="en">
<head>
<meta charset="utf-8">
<title>Kelta Core Fitness – Grand Opening</title>
<link href="https://fonts.googleapis.com/css2?family=Montserrat:wght@400;500;700;800&family=Open+Sans:wght@700&family=Exo+2:wght@800&family=Noto+Serif:wght@700&display=swap" rel="stylesheet">
<style>
  :root{
    --backdrop:#6e5842;
    --paper:#ffffff;
    --salmon:#f4967b;
    --peach:#fbc48a;
    --orange-gold:#f2b35a;
    --grey-dark:#6f6f6f;
    --grey-mid:#7d7d7d;
    --grey-light:#a9a9a9;
    --photo-deep:#b77d45;
    --photo-warm:#dba46a;
    --photo-light:#f3d5ad;
    --star:#f7b36b;
  }
  *{margin:0;padding:0;box-sizing:border-box}
  html,body{width:900px;height:1200px;overflow:hidden}
  body{background:var(--backdrop);position:relative;font-family:"Montserrat",sans-serif}

  .poster{position:absolute;left:75px;top:38px;width:753px;height:1127px;background:var(--paper);overflow:hidden;box-shadow:0 6px 24px rgba(0,0,0,.45)}

  .banner{position:absolute;left:0;top:0;width:753px;height:88px}
  .banner-text{position:absolute;left:0;top:8px;width:753px;text-align:center;font-family:"Noto Serif",serif;font-weight:700;font-size:54px;letter-spacing:1px;color:#8c8c8c;
    text-shadow:1px 1px 0 #fff,-1px -1px 0 #fff,1px -1px 0 #fff,-1px 1px 0 #fff,0 3px 4px rgba(0,0,0,.35)}

  .brand-name{position:absolute;left:0;width:753px;text-align:center;color:var(--grey-mid);font-family:"Montserrat",sans-serif;font-weight:400}
  .brand-main{top:96px;font-size:78px;letter-spacing:14px;padding-left:14px}
  .brand-sub{top:192px;left:210px;width:400px;font-size:56px;letter-spacing:20px;color:var(--grey-light)}

  .brand-dot{position:absolute;left:13px;top:187px;width:172px;height:172px;border-radius:50%;background:var(--salmon);border:10px solid var(--paper);box-shadow:0 2px 8px rgba(0,0,0,.15)}

  .photo{position:absolute;left:0;top:262px;width:753px;height:540px}

  .perks{position:absolute;left:30px;top:410px;list-style:none}
  .perks li{display:flex;align-items:center;height:69px;font-family:"Open Sans",sans-serif;font-weight:700;font-size:33px;color:#fff;text-shadow:0 2px 4px rgba(90,55,20,.6)}
  .perks svg{width:32px;height:32px;margin-right:12px;flex:none}

  .phone{position:absolute;left:0;top:800px;width:753px;text-align:center;font-family:"Exo 2",sans-serif;font-weight:800;font-size:92px;letter-spacing:1px;color:var(--grey-dark);
    text-shadow:2px 2px 0 #fff,-2px -2px 0 #fff,2px -2px 0 #fff,-2px 2px 0 #fff,0 4px 6px rgba(0,0,0,.35)}
  .cta{position:absolute;left:0;top:893px;width:753px;text-align:center;font-family:"Exo 2",sans-serif;font-weight:800;font-size:64px;letter-spacing:3px;color:var(--orange-gold);text-shadow:0 2px 3px rgba(0,0,0,.3)}

  .web-band{position:absolute;left:0;top:977px;width:753px;height:60px;background:var(--grey-mid);display:flex;align-items:center;justify-content:center;font-weight:800;font-size:33px;letter-spacing:1px;color:#fff}
  .social-band{position:absolute;left:0;top:1040px;width:753px;height:87px;background:var(--peach);display:flex;align-items:center;justify-content:center;gap:20px}
  .social-square{width:52px;height:52px;background:#c98a4e}
  .handle{font-weight:500;font-size:48px;color:var(--grey-mid);letter-spacing:1px;text-shadow:0 0 6px #fff}
</style>
</head>
<body>
  <main class="poster">
    <svg class="banner" viewBox="0 0 753 88" aria-hidden="true">
      <polygon points="65,0 710,0 688,88 90,88" fill="var(--salmon)"/>
    </svg>
    <h2 class="banner-text">GRAND OPENING</h2>

    <h1>
      <span class="brand-name brand-main">KELTA CORE</span>
      <span class="brand-name brand-sub">fitness</span>
    </h1>

    <svg class="photo" viewBox="0 0 753 540" role="img" aria-label="Photo of a woman in a sports top looking over a sunlit field with a dirt track">
      <defs>
        <linearGradient id="sky" x1="0" y1="0" x2="0" y2="1">
          <stop offset="0" stop-color="var(--photo-light)"/>
          <stop offset=".35" stop-color="var(--photo-warm)"/>
          <stop offset=".7" stop-color="var(--photo-deep)"/>
          <stop offset="1" stop-color="var(--photo-warm)"/>
        </linearGradient>
        <radialGradient id="sun" cx=".72" cy=".2" r=".5">
          <stop offset="0" stop-color="#fff4e0" stop-opacity=".9"/>
          <stop offset="1" stop-color="#fff4e0" stop-opacity="0"/>
        </radialGradient>
        <linearGradient id="fade" x1="0" y1="0" x2="0" y2="1">
          <stop offset=".72" stop-color="#fff" stop-opacity="0"/>
          <stop offset=".98" stop-color="#fff" stop-opacity="1"/>
        </linearGradient>
      </defs>
      <path d="M0 40 C200 -10 460 5 753 30 L753 540 L0 540 Z" fill="url(#sky)"/>
      <path d="M0 40 C200 -10 460 5 753 30 L753 540 L0 540 Z" fill="url(#sun)"/>
      <path d="M260 28 C450 -8 620 8 753 40" fill="none" stroke="var(--salmon)" stroke-width="4" opacity=".7"/>
      <rect width="753" height="540" fill="url(#fade)"/>
    </svg>

    <div class="brand-dot" aria-hidden="true"></div>

    <ul class="perks">
      <li><svg viewBox="0 0 24 24" aria-hidden="true"><polygon points="12,1 15,9 23,9 16.5,14 19,22 12,17 5,22 7.5,14 1,9 9,9" fill="var(--star)"/></svg>FREE introductory class</li>
      <li><svg viewBox="0 0 24 24" aria-hidden="true"><polygon points="12,1 15,9 23,9 16.5,14 19,22 12,17 5,22 7.5,14 1,9 9,9" fill="var(--star)"/></svg>Personalized instruction</li>
      <li><svg viewBox="0 0 24 24" aria-hidden="true"><polygon points="12,1 15,9 23,9 16.5,14 19,22 12,17 5,22 7.5,14 1,9 9,9" fill="var(--star)"/></svg>Body sculpting workout</li>
      <li><svg viewBox="0 0 24 24" aria-hidden="true"><polygon points="12,1 15,9 23,9 16.5,14 19,22 12,17 5,22 7.5,14 1,9 9,9" fill="var(--star)"/></svg>Results training</li>
      <li><svg viewBox="0 0 24 24" aria-hidden="true"><polygon points="12,1 15,9 23,9 16.5,14 19,22 12,17 5,22 7.5,14 1,9 9,9" fill="var(--star)"/></svg>Fun, supportive atmosphere</li>
    </ul>

    <p class="phone">1-818-555-CORE</p>
    <p class="cta">TRY A CLASS TODAY!</p>

    <div class="web-band">WWW.KELTACOREFITNESS.EXAMPLE</div>
    <div class="social-band">
      <span class="social-square" aria-hidden="true"></span>
      <span class="handle">@KELTACOREFITNESS</span>
    </div>
  </main>
</body>
</html>
```